RK Bastone Construction Inc.

Design a new business card for our construction company
To be removed from current card:
Delete 25 years
Delete Tenant fit up Renovations section

```html
<!DOCTYPE html>
<html lang="en">
<head>
<meta charset="utf-8">
<title>RK Bastone Construction Inc. — Business Card</title>
<link rel="stylesheet" href="https://fonts.googleapis.com/css2?family=Exo+2:wght@400;500;800&family=Montserrat:wght@500&display=swap">
<style>
  :root {
    --backdrop: #2d2d2d;
    --card: #000000;
    --purple: #5a2d8c;
    --teal: #1f7b6f;
    --white: #f2f2f2;
  }
  * { box-sizing: border-box; margin: 0; padding: 0; }
  html, body { width: 1200px; height: 1015px; overflow: hidden; }
  body {
    background: var(--backdrop);
    display: flex;
    flex-direction: column;
    align-items: center;
    justify-content: center;
    gap: 56px;
    font-family: "Exo 2", sans-serif;
    color: var(--white);
  }
  .card {
    width: 630px;
    height: 360px;
    background: var(--card);
    position: relative;
    box-shadow: 0 14px 30px rgba(0,0,0,.45);
    overflow: hidden;
  }

  /* Front */
  .card--front {
    display: flex;
    flex-direction: column;
    align-items: center;
    justify-content: center;
    gap: 18px;
  }
  .brand-name {
    font-family: "Exo 2", sans-serif;
    font-weight: 800;
    font-size: 36px;
    line-height: 1.05;
    letter-spacing: 2px;
    text-transform: uppercase;
    color: var(--teal);
    text-align: left;
  }
  .brand-name span { display: block; }
  .tagline {
    font-family: "Montserrat", sans-serif;
    font-weight: 500;
    font-size: 14px;
    letter-spacing: 1px;
    text-transform: uppercase;
    color: var(--white);
    display: flex;
    align-items: center;
    gap: 8px;
  }
  .tagline .dot {
    width: 6px; height: 6px; border-radius: 50%;
    background: var(--purple);
  }

  /* Back */
  .contact {
    position: absolute;
    left: 48px;
    top: 52px;
    width: 400px;
  }
  .person-name {
    font-weight: 800;
    font-size: 22px;
    letter-spacing: 2px;
    text-transform: uppercase;
  }
  .person-name .first { color: var(--purple); }
  .person-name .last { color: var(--teal); }
  .rule {
    width: 150px;
    height: 1px;
    background: var(--teal);
    margin: 22px 0 20px 40px;
  }
  .contact-list { list-style: none; }
  .contact-list li {
    display: flex;
    align-items: center;
    gap: 10px;
    font-size: 15px;
    line-height: 24px;
    padding-left: 40px;
  }
  .contact-list svg { width: 15px; height: 15px; flex: none; }
  .contact-list .accent { color: var(--teal); }
  .address {
    padding-left: 80px;
    font-size: 16px;
    line-height: 24px;
    font-style: normal;
  }
  .rule--address { margin-left: 80px; }

  .back-brand {
    position: absolute;
    right: 34px;
    top: 50%;
    writing-mode: vertical-rl;
    transform: translateY(-50%) rotate(180deg);
    white-space: nowrap;
    font-weight: 800;
    font-size: 22px;
    line-height: 1.1;
    letter-spacing: 2px;
    text-transform: uppercase;
    color: var(--teal);
  }
  .back-brand span { display: block; }
</style>
</head>
<body>

  <section class="card card--front" aria-label="Business card front">
    <div>
      <h1 class="brand-name"><span>RK Bastone</span><span>Construction Inc.</span></h1>
    </div>
    <p class="tagline">Office <span class="dot"></span> Retail <span class="dot"></span> Institutional</p>
  </section>

  <section class="card card--back" aria-label="Business card back">
    <div class="contact">
      <h2 class="person-name"><span class="first">Marco</span> <span class="last">Bastone</span></h2>
      <div class="rule"></div>
      <ul class="contact-list">
        <li>
          <svg viewBox="0 0 24 24" fill="none" stroke="var(--teal)" stroke-width="2.4" stroke-linecap="round" stroke-linejoin="round"><path d="M22 16.9v3a2 2 0 0 1-2.2 2 19.8 19.8 0 0 1-8.6-3.1 19.5 19.5 0 0 1-6-6A19.8 19.8 0 0 1 2.1 4.2 2 2 0 0 1 4.1 2h3a2 2 0 0 1 2 1.7c.1 1 .4 1.9.7 2.8a2 2 0 0 1-.5 2.1L8 9.9a16 16 0 0 0 6 6l1.3-1.3a2 2 0 0 1 2.1-.4c.9.3 1.8.6 2.8.7a2 2 0 0 1 1.8 2z"/></svg>
          613-555-0142 ext.221
        </li>
        <li>
          <svg viewBox="0 0 24 24" fill="none" stroke="var(--teal)" stroke-width="2.4" stroke-linecap="round"><rect x="6" y="2" width="12" height="20" rx="2"/><line x1="12" y1="18" x2="12" y2="18"/></svg>
          613-555-0178
        </li>
        <li>
          <svg viewBox="0 0 24 24" fill="none" stroke="var(--teal)" stroke-width="2.4" stroke-linejoin="round"><rect x="2" y="5" width="20" height="14"/><path d="M2 5l10 8 10-8"/></svg>
          marco@rkbastoneconst.ca
        </li>
        <li>
          <svg viewBox="0 0 24 24" fill="none" stroke="var(--teal)" stroke-width="2.2"><circle cx="12" cy="12" r="10"/><path d="M2 12h20M12 2a15 15 0 0 1 0 20M12 2a15 15 0 0 0 0 20"/></svg>
          <span>www.<span class="accent">rkbastoneconstruction</span>.ca</span>
        </li>
      </ul>
      <div class="rule rule--address"></div>
      <address class="address">
        2180 Halden Rd., Suite 100<br>
        Ottawa, On K1B 4R7
      </address>
    </div>
    <p class="back-brand"><span>RK Bastone</span><span>Construction Inc.</span></p>
  </section>

</body>
</html>
```